Pro work for a Landing Page for Mobile and PC in ITALIAN and ENGLISH language

We need a design for the mobile and desktop landing page you see in the enclosed text. 2 versions. We attach a copy to give an idea of style we are used to give to our landing pages, so as to understand that we are looking for quality, not only amatoriale graphic.

On Monday 1st we'll deliver design already made for the Gift Card and for Brivoza logo. We'll also provide images for the play to earn Game we talk about in second part of the Landing page

Please provide two versions: one in Italian and the other in English, Both for iOS and Android Mobile and Windows and Mac Pc.

It must be very professional work.

Precise delivery time by which design must be full ready -after usual revisions: Friday, January 5th.

Please note that no work will be accepted after this date, as it will be used on presentation the day after, Saturday January 6th

Attached at this please find Text for Landing page both in Italian and English and 3 samples from a landing page we produced and it is the way we would like present one (https://go.tellurquest.com/tellur-quest-pro/).

Target Market(s)

General public, any age, income, scholarship

Industry/Entity Type

Make money Opportunity

Number of Pages Required

1 page

Font styles to use
Serif

Requirements
Must have
• Images I'll provide on Jan 1st: Orbo Bonus Gift Card; Brivoza logo; KOR Play to earn Game
Nice to have
• We enclosed a landing page example. Another one is this https://events.korlintra.io/landing-viral/ Please note that the one we attached is the style we want for this one we are ordering.
Should not have
• Poor graphics or style. It must seem "rich"

```html
<!DOCTYPE html>
<html lang="en">
<head>
<meta charset="UTF-8">
<title>Brivoza – Orbo Bonus Gift Card</title>
<link rel="stylesheet" href="https://fonts.googleapis.com/css2?family=Inter:wght@700&family=Kurale&family=Michroma&family=Exo+2:wght@300&display=swap">
<style>
  :root {
    --bg-deep: #12022f;
    --bg-glow: #0a3f86;
    --gold: #c9a227;
    --yellow: #ffd600;
    --white: #ffffff;
    --muted: #b8b8cc;
    --ink: #111111;
  }
  * { margin: 0; padding: 0; box-sizing: border-box; }
  html, body { width: 1200px; height: 768px; overflow: hidden; }
  body {
    background: var(--bg-deep);
    font-family: "Kurale", Georgia, serif;
    color: var(--white);
  }
  .landing {
    position: relative;
    width: 1200px;
    height: 768px;
    overflow: hidden;
    background:
      radial-gradient(ellipse 520px 380px at 520px 420px, rgba(10,63,134,0.85), rgba(10,63,134,0) 75%),
      radial-gradient(ellipse 700px 500px at 600px 380px, rgba(40,30,110,0.6), rgba(18,2,47,0) 80%),
      var(--bg-deep);
  }
  .brand {
    position: absolute;
    top: 52px; left: 0; width: 100%;
    text-align: center;
    font-family: "Inter", Arial, sans-serif;
    font-weight: 700;
    font-size: 48px;
    color: var(--gold);
    letter-spacing: -0.5px;
  }
  .hero-art {
    position: absolute;
    left: 42px; top: 154px;
    width: 580px; height: 514px;
    border-radius: 40%;
    background:
      radial-gradient(circle at 42% 45%, rgba(60,170,210,0.75), rgba(40,70,140,0.45) 45%, rgba(110,60,200,0.2) 70%, rgba(18,2,47,0) 80%);
  }
  .offer {
    position: absolute;
    left: 625px; top: 160px;
    width: 490px;
    text-align: center;
  }
  .offer-kicker { font-size: 25px; line-height: 1.2; }
  .offer-name {
    margin-top: 22px;
    font-family: "Michroma", Arial, sans-serif;
    font-size: 44px;
    line-height: 1;
    letter-spacing: 1px;
  }
  .offer-lead {
    margin-top: 24px;
    font-size: 23px;
    line-height: 1.32;
  }
  .offer-product {
    margin-top: 22px;
    font-family: "Michroma", Arial, sans-serif;
    font-size: 50px;
    line-height: 1;
    color: var(--yellow);
  }
  .offer-perk {
    margin-top: 18px;
    font-family: "Exo 2", Arial, sans-serif;
    font-weight: 300;
    font-size: 25px;
    display: flex; align-items: center; justify-content: center; gap: 12px;
  }
  .perk-dot { width: 26px; height: 26px; border-radius: 50%; background: #f4c543; }
  .cta {
    display: block;
    margin-top: 22px;
    height: 75px;
    line-height: 75px;
    border-radius: 10px;
    background: var(--yellow);
    color: var(--ink);
    font-size: 26px;
    text-decoration: none;
  }
  .offer-note {
    margin-top: 20px;
    font-size: 20px;
    line-height: 1.4;
    color: var(--muted);
  }
</style>
</head>
<body>
  <main class="landing">
    <h1 class="brand">Brivoza</h1>
    <div class="hero-art" role="img" aria-label="Friendly blue robot holding a purple gift box with a yellow ribbon over a glowing network"></div>
    <section class="offer">
      <p class="offer-kicker">Treat yourself to a precious gift now!</p>
      <h2 class="offer-name">ORBO BONUS</h2>
      <p class="offer-lead">Yours, completely free, the Gift Card that you can use all over the world with which...</p>
      <h2 class="offer-product">GIFT CARD</h2>
      <p class="offer-perk">You Receive Gifts! <span class="perk-dot"></span></p>
      <a class="cta" href="#">Request your Gift Card here for free</a>
      <p class="offer-note">From February, you will be able to download it, in a VIRTUAL version, without any costs or commitments!</p>
    </section>
  </main>
</body>
</html>
```